Notary Signing Agent Need Business card Design

Need a Business card design for my new company. RT Velo-Brisk LLC
Mobile Notary Signing Agent. I go to the customer for closing of Mortgage's Documents . possible signs of honesty, integrity and confidentiality.

Work with Title company to Notary Mortgage closing.

My Target Market is Title companies. Banks and Financial Institution.

Color Blue to Black Professional ) if needed some Green Little Red

And possible a company logo.

Mobile ( travel to clients ) Integrity, Honest Trustworthy. A show of Professional services.

Would like company name and my name on card

Use both sides and front with business name and my name. phone numbers.

Target Market(s)

Title company, Banks mortgage company

Industry/Entity Type

Travel

Contact Information for Business Card

Notary, Certified signing agent, Mobile

Colors
0455a3

Requirements
Must have
• Name of company , owners name phone number,
Nice to have
• blue and black color like a professional look but not limit to these only.
• a stand out from other cards .

```html
<!DOCTYPE html>
<html lang="en">
<head>
<meta charset="utf-8">
<title>RT Velo-Brisk LLC — Business Card</title>
<link href="https://fonts.googleapis.com/css2?family=Arimo:wght@400;700&display=swap" rel="stylesheet">
<style>
  :root {
    --stage: #6b6c6c;
    --brand-blue: #0455a3;
    --brand-blue-light: #1d74c6;
    --brand-blue-deep: #033f7e;
    --ink: #141414;
    --paper: #ffffff;
    --rule-grey: #8a8a8a;
  }
  * { margin: 0; padding: 0; box-sizing: border-box; }
  html, body { width: 1200px; height: 1200px; overflow: hidden; }
  body {
    background: var(--stage);
    font-family: "Arimo", Arial, sans-serif;
    display: flex;
    flex-direction: column;
    align-items: center;
    justify-content: center;
    gap: 90px;
  }
  .card {
    position: relative;
    width: 700px;
    height: 400px;
    overflow: hidden;
  }
  .card-art { position: absolute; inset: 0; width: 100%; height: 100%; }

  /* Front */
  .card-front .company-name {
    position: absolute;
    left: 54px;
    top: 272px;
    color: var(--paper);
    font-weight: 700;
    font-size: 34px;
    letter-spacing: 0.5px;
    text-transform: uppercase;
  }

  /* Back */
  .card-back .company-name {
    position: absolute;
    right: 42px;
    top: 96px;
    color: var(--brand-blue);
    font-weight: 700;
    font-size: 36px;
    letter-spacing: 0.5px;
    text-transform: uppercase;
  }
  .holder {
    position: absolute;
    right: 26px;
    top: 221px;
    text-align: right;
    color: var(--paper);
    line-height: 1;
  }
  .holder-name {
    font-weight: 700;
    font-size: 17px;
    letter-spacing: 0.5px;
    text-transform: uppercase;
  }
  .holder-role {
    font-weight: 700;
    font-size: 9px;
    letter-spacing: 1px;
    margin-top: 3px;
    text-transform: uppercase;
  }
  .contact-list {
    position: absolute;
    left: 34px;
    top: 214px;
    list-style: none;
    color: var(--paper);
    font-size: 13px;
    line-height: 19px;
  }
  .contact-list li { display: flex; align-items: center; gap: 8px; }
  .contact-list svg { width: 11px; height: 11px; fill: var(--paper); }
</style>
</head>
<body>

  <section class="card card-front" aria-label="Business card front">
    <svg class="card-art" viewBox="0 0 700 400" aria-hidden="true">
      <defs>
        <radialGradient id="frontGlow" cx="0.42" cy="0.4" r="0.75">
          <stop offset="0" stop-color="var(--brand-blue-light)"/>
          <stop offset="0.6" stop-color="var(--brand-blue)"/>
          <stop offset="1" stop-color="var(--brand-blue-deep)"/>
        </radialGradient>
      </defs>
      <rect width="700" height="400" fill="url(#frontGlow)"/>
    </svg>
    <h1 class="company-name">RT Velo-Brisk LLC.</h1>
  </section>

  <section class="card card-back" aria-label="Business card back">
    <svg class="card-art" viewBox="0 0 700 400" aria-hidden="true">
      <defs>
        <linearGradient id="backBlue" x1="0" y1="0" x2="1" y2="1">
          <stop offset="0" stop-color="var(--brand-blue-light)"/>
          <stop offset="0.55" stop-color="var(--brand-blue)"/>
          <stop offset="1" stop-color="var(--brand-blue-deep)"/>
        </linearGradient>
      </defs>
      <rect width="700" height="400" fill="url(#backBlue)"/>
      <polygon class="band-rule" points="0,170 205,170 258,212 700,212 700,216 256,216 203,176 0,176" fill="var(--rule-grey)"/>
      <polygon class="band-dark" points="268,212 700,212 700,256 300,256" fill="var(--ink)"/>
      <polygon class="paper-field" points="0,0 700,0 700,212 258,212 205,170 0,170" fill="var(--paper)"/>
    </svg>

    <h2 class="company-name">RT Velo-Brisk LLC.</h2>

    <div class="holder">
      <p class="holder-name">Daniel R Hoyt</p>
      <p class="holder-role">Owner</p>
    </div>

    <ul class="contact-list">
      <li>
        <svg viewBox="0 0 24 24" aria-hidden="true"><path d="M6.6 10.8a15.1 15.1 0 0 0 6.6 6.6l2.2-2.2a1 1 0 0 1 1-.25 11.4 11.4 0 0 0 3.6.57 1 1 0 0 1 1 1V20a1 1 0 0 1-1 1A17 17 0 0 1 3 4a1 1 0 0 1 1-1h3.5a1 1 0 0 1 1 1c0 1.25.2 2.45.57 3.57a1 1 0 0 1-.25 1z"/></svg>
        555-014-2287
      </li>
      <li>
        <svg viewBox="0 0 24 24" aria-hidden="true"><path d="M7 1h10a2 2 0 0 1 2 2v18a2 2 0 0 1-2 2H7a2 2 0 0 1-2-2V3a2 2 0 0 1 2-2zm0 3v14h10V4zm5 15.5a1 1 0 1 0 0 2 1 1 0 0 0 0-2z"/></svg>
        555-013-6409
      </li>
      <li>
        <svg viewBox="0 0 24 24" aria-hidden="true"><path d="M2 5h20v14H2zm2 2v.5l8 5 8-5V7zm0 2.9V17h16V9.9l-8 5z"/></svg>
        hello@velobrisk.com
      </li>
    </ul>
  </section>

</body>
</html>
```